Recruiting agency looking for a newsletter design

We need to design a newsletter that will be sent by e-mail to our clients database. This communication announces a new milestone for our company.

We need it to convey high professionalism, elegance ad luxury. It needs to catch the reader’s attention.

The background needs to be light shiny silver, not flat gray, not dark silver. Some effects can give dimension to the content. We need a very impactful communication.

You will find attached:

- The content that needs to appear on the newsletter
- Pictures “moodboard” that you can take into consideration for the overall “atmosphere” and “emotion” that the design needs to convey. Please DO NOT include any of these images in the newsletter itself. They are just here to help you get the idea of the type of image we want to convey as a company with this communication.
- Company logo
- Please note that I will provide you later on with a URL link to include to the newsletter.

```html
<!DOCTYPE html>
<html lang="en">
<head>
<meta charset="utf-8">
<title>2021 New Era – New Fees</title>
<link rel="stylesheet" href="https://fonts.googleapis.com/css2?family=Archivo+Black&family=Arimo&family=Roboto+Condensed:wght@400&display=swap">
<style>
  :root {
    --navy: #141f4a;
    --crimson: #d5143f;
    --crimson-deep: #c20f39;
    --silver: #cdcdd1;
    --silver-light: #dadade;
    --white: #ffffff;
    --muted: #444444;
    --photo-dark: #0a1d20;
    --photo-mid: #2a3c40;
  }
  * { margin: 0; padding: 0; box-sizing: border-box; }
  html, body { width: 749px; height: 1200px; overflow: hidden; background: var(--white); }
  body { position: relative; font-family: "Archivo Black", sans-serif; color: var(--navy); }

  .preheader {
    position: absolute; top: 36px; left: 0; width: 749px; text-align: center;
    font-family: "Arimo", sans-serif; font-size: 12px; line-height: 17px; color: var(--muted);
  }
  .preheader a { color: var(--crimson); }

  .card {
    position: absolute; left: 143px; top: 92px; width: 463px; height: 993px;
    border-radius: 12px;
    background: linear-gradient(160deg, var(--silver-light) 0%, var(--silver) 45%, #c6c6cb 100%);
  }

  .hero-title {
    position: absolute; left: 20px; top: 58px; width: 425px; height: 189px;
    background: var(--white); text-align: center;
  }
  .hero-year { display: block; padding-top: 28px; font-size: 92px; line-height: 90px; letter-spacing: -1px; color: var(--navy); }
  .hero-tagline { display: block; margin-top: 6px; font-size: 33px; line-height: 38px; color: var(--navy); }
  .hero-tagline .fees { font-size: 26px; color: var(--crimson); }

  .hero-photo {
    position: absolute; left: 20px; top: 247px; width: 425px; height: 275px;
    background: radial-gradient(ellipse at 50% 55%, var(--photo-mid) 0%, var(--photo-dark) 70%);
  }

  .fees-panel {
    position: absolute; left: 20px; top: 522px; width: 425px; height: 173px;
    background: var(--white);
  }
  .fees-panel svg { position: absolute; left: 0; top: 0; }
  .fee { position: absolute; text-align: center; }
  .fee-label { font-size: 16px; line-height: 18px; }
  .fee-value { font-size: 52px; line-height: 56px; margin-top: 8px; }
  .fee--executive { left: 0; width: 186px; top: 46px; color: var(--white); }
  .fee--other { left: 254px; width: 162px; top: 44px; color: var(--navy); }
  .fee--other .fee-value { margin-left: 14px; }

  .cta {
    position: absolute; left: 0; top: 728px; width: 463px; text-align: center;
  }
  .cta-headline { font-size: 20px; line-height: 28px; color: var(--navy); }
  .cta-headline .join { font-size: 25px; color: var(--crimson); }
  .cta-row {
    display: flex; justify-content: center; align-items: center; gap: 11px; margin-top: 8px;
    font-family: "Roboto Condensed", sans-serif;
  }
  .cta-note { font-size: 17px; color: var(--navy); }
  .cta-button {
    display: inline-block; width: 121px; height: 34px; line-height: 34px; border-radius: 17px;
    background: var(--crimson); color: var(--white); font-size: 17px; text-decoration: none;
  }

  .brand {
    position: absolute; left: 0; top: 910px; width: 463px;
    display: flex; justify-content: center; align-items: center; gap: 10px;
  }
  .brand-dot { width: 14px; height: 14px; border-radius: 50%; background: var(--navy); }
  .brand-name { font-size: 18px; letter-spacing: 3px; color: var(--navy); }
</style>
</head>
<body>
  <div class="preheader">
    Is this email not displaying correctly?<br>
    <a href="#">View it in your browser.</a>
  </div>

  <main class="card">
    <section class="hero-title">
      <span class="hero-year">2021</span>
      <span class="hero-tagline">NEW ERA - <span class="fees">(NEW FEES)</span></span>
    </section>

    <div class="hero-photo" role="img" aria-label="Close-up photo of a chrome hood ornament on a dark luxury car"></div>

    <section class="fees-panel">
      <svg width="425" height="173" viewBox="0 0 425 173" aria-hidden="true">
        <defs>
          <linearGradient id="feeRed" x1="0" y1="0" x2="0" y2="1">
            <stop offset="0" stop-color="#dd2a50"/>
            <stop offset="1" stop-color="#c20f39"/>
          </linearGradient>
        </defs>
        <polygon points="0,0 255,0 255,91 169,91 169,173 0,173" fill="url(#feeRed)"/>
      </svg>
      <div class="fee fee--executive">
        <div class="fee-label">Top managers<br>Executives</div>
        <div class="fee-value">50%</div>
      </div>
      <div class="fee fee--other">
        <div class="fee-label">All other<br>appointments</div>
        <div class="fee-value">21%</div>
      </div>
    </section>

    <section class="cta">
      <p class="cta-headline"><span class="join">JOIN US</span> in shaping the future<br>of recruitment</p>
      <div class="cta-row">
        <span class="cta-note">For more information</span>
        <a class="cta-button" href="#">CLICK HERE</a>
      </div>
    </section>

    <footer class="brand">
      <span class="brand-dot"></span>
      <span class="brand-name">HARROW &amp; VALE</span>
    </footer>
  </main>
</body>
</html>
```